Defense Attorney Business Card Design Project/ Stationary

I am looking for a distinctive business card design for my solo law practice.
I practice criminal defense, both juvenile and adult, including DUI. I am a very experienced attorney with prior military experience. The design should convey a traditional, old school flair, but not be too stodgy or uptight. Some color. My logo should appear.

Project Deadline Extended Reason: I misunderstood how this project works and I was not prepared with my logo when this project ran the first time. Added Thursday, November 13, 2014

Reason: I was sent overseas on military duty last year, which interrupted this project. Thank you for your participation... I hope we can get this done this week! Thank you, Des

Target Market(s)

Regular everyday people looking for strong, knowledgeable, authoritative representation while they are faced with criminal charges. Many have never been charged with a crime before. A reassuring air is therefore desired.

Industry/Entity Type

Business

Contact Information for Business Card

My information is:
Desmond R. Whitcombe, Attorney at Law
735 Linden Avenue Suite 300
Oakland, California 94618
Tel: (510) 555-0183
Fax: (510) 555-0162
email: deswhitcombelaw@mailbrook.net
web: www.deswhitcombelaw.net

Font styles to use
Serif
Sans Serif
Decorative

Colors
0255a3
ffffff

Requirements
Must have
• Sharp lines, bold elements. Conservative use of colors, such as deep blues, burgundy, grays for example.
• While my logo says "Des Whitcombe", it should be modified to show "Desmond R. Whitcombe".
Should not have
• Cliche imagery such as scales of justice, gavels, Tower of Varenholt, etc.

```html
<!DOCTYPE html>
<html lang="en">
<head>
<meta charset="utf-8">
<title>Desmond R. Whitcombe – Business Card</title>
<link rel="stylesheet" href="https://fonts.googleapis.com/css2?family=Arimo:wght@400;700&display=swap">
<style>
  :root {
    --page: #ffffff;
    --card-dark: #33363b;
    --card-light: #ffffff;
    --card-edge: #9a9da1;
    --mark-grey: #a7abb0;
    --navy: #234a66;
    --ink: #2b2b2b;
    --muted: #8a8d91;
    --divider: #b3b6ba;
  }
  * { margin: 0; padding: 0; box-sizing: border-box; }
  html, body {
    width: 1200px; height: 900px; overflow: hidden;
    background: var(--page);
    font-family: "Arimo", Arial, sans-serif;
  }
  .canvas { position: relative; width: 1200px; height: 900px; }

  .card {
    position: absolute; left: 218px; width: 763px;
    border: 1px solid var(--card-edge);
  }
  .card--back {
    top: 11px; height: 430px;
    background: var(--card-dark);
    display: flex; align-items: center; justify-content: center;
  }
  .card--front { top: 459px; height: 429px; background: var(--card-light); }

  .wordmark {
    font-family: "Arimo", Arial, sans-serif;
    font-weight: 700; white-space: nowrap;
  }
  .wordmark--back { color: var(--mark-grey); font-size: 46px; }
  .wordmark--front {
    position: absolute; left: 0; width: 360px; top: 200px;
    text-align: center; color: var(--navy); font-size: 26px; line-height: 32px;
  }

  .divider {
    position: absolute; left: 359px; top: 60px;
    width: 3px; height: 308px; background: var(--divider);
  }

  .details { position: absolute; left: 399px; top: 70px; color: var(--ink); }
  .details__name { font-weight: 700; font-size: 28px; color: var(--navy); line-height: 32px; }
  .details__title { font-size: 18px; color: var(--muted); line-height: 24px; }

  .contact { list-style: none; margin-top: 30px; }
  .contact__item {
    display: flex; align-items: center; height: 29.5px;
    font-size: 21px; line-height: 1; white-space: nowrap;
  }
  .contact__icon { width: 24px; height: 20px; margin-right: 13px; fill: var(--navy); flex: none; }

  .address { display: flex; margin-top: 22px; font-size: 21px; line-height: 28px; white-space: nowrap; }
  .address__icon { width: 18px; height: 32px; margin-right: 15px; fill: var(--navy); flex: none; }
</style>
</head>
<body>
<main class="canvas">

  <section class="card card--back" aria-label="Card back">
    <span class="wordmark wordmark--back">Desmond R. Whitcombe</span>
  </section>

  <section class="card card--front" aria-label="Card front">
    <span class="wordmark wordmark--front">Desmond R. Whitcombe</span>

    <div class="divider"></div>

    <div class="details">
      <h1 class="details__name">Des Whitcombe</h1>
      <p class="details__title">Attorney</p>

      <ul class="contact">
        <li class="contact__item">
          <svg class="contact__icon" viewBox="0 0 24 20" aria-hidden="true">
            <path d="M2 8c0-4 5-6 10-6s10 2 10 6v2h-5V7c-2-.8-8-.8-10 0v3H2z"/>
            <path d="M5 11l3-3h8l3 3v7H5z"/><circle cx="12" cy="14" r="2.3" fill="#fff"/>
          </svg>
          <span>(510) 555-0183</span>
        </li>
        <li class="contact__item">
          <svg class="contact__icon" viewBox="0 0 24 20" aria-hidden="true">
            <path d="M7 1h10v6H7z"/><path d="M4 8h16v8H4z"/><path d="M7 13h10v6H7z" fill="#fff" stroke="#234a66" stroke-width="2"/>
          </svg>
          <span>(510) 555-0162</span>
        </li>
        <li class="contact__item">
          <svg class="contact__icon" viewBox="0 0 24 20" aria-hidden="true">
            <path d="M1 3h22v15H1z"/><path d="M2 4l10 8 10-8" fill="none" stroke="#fff" stroke-width="1.8"/>
          </svg>
          <span>deswhitcombelaw@mailbrook.net</span>
        </li>
        <li class="contact__item">
          <svg class="contact__icon" viewBox="0 0 24 20" aria-hidden="true">
            <circle cx="12" cy="10" r="8"/>
            <g fill="none" stroke="#fff" stroke-width="1.4">
              <ellipse cx="12" cy="10" rx="3.5" ry="8"/><path d="M4 10h16M5.5 6h13M5.5 14h13"/>
            </g>
          </svg>
          <span>www.deswhitcombelaw.net</span>
        </li>
      </ul>

      <div class="address">
        <svg class="address__icon" viewBox="0 0 18 32" aria-hidden="true">
          <path d="M9 1C4.3 1 1 4.5 1 9c0 6 8 20 8 20s8-14 8-20c0-4.5-3.3-8-8-8z"/>
          <circle cx="9" cy="9" r="3" fill="#fff"/>
        </svg>
        <p>735 Linden Avenue Suite 300<br>Oakland, California 94618</p>
      </div>
    </div>
  </section>

</main>
</body>
</html>
```